Volt'n Electrical Business Card Design

FRONT OF CARD: should highlight the company logo ( please use image attached) and in small font in the bottom corner must have REC 48193

BACK OF CARD : Company logo at the top, underneath the logo have my name Owen Tate under my name in smaller font Qualified Electrician.
Details to also include are Mobile: 0438257109 E-mail: voltnelectrical@mailbox-example.net

Front and back of card please try to use similar colours as used in the logo. (Blues, greys, black and white)

The logo was created on this website so if you need a different file type of the logo please notify me.

Thanks, Owen

Industry/Entity Type

Business

Contact Information for Business Card

Details are in project description.

Colors
3176b5

Requirements
Must have
• Company logo and contact details

```html
<!DOCTYPE html>
<html lang="en">
<head>
<meta charset="utf-8">
<title>Volt'n Electrical – Business Card</title>
<link rel="stylesheet" href="https://fonts.googleapis.com/css2?family=Michroma&family=Open+Sans:wght@400;600&display=swap">
<style>
  :root {
    --backdrop: #e4e4e4;
    --navy: #293d52;
    --navy-text: #2b3a4c;
    --blue: #3a9ad9;
    --white: #ffffff;
    --light-grey: #e6e9ed;
    --grey-text: #3d4a58;
    --rec-text: #c9d3de;
  }
  * { box-sizing: border-box; margin: 0; padding: 0; }
  html, body {
    width: 1200px; height: 852px; overflow: hidden;
    background: var(--backdrop);
  }
  .sheet {
    position: relative; width: 1200px; height: 852px;
    display: flex; align-items: center; justify-content: center; gap: 40px;
  }
  .card {
    position: relative; width: 520px; height: 300px;
    border-radius: 24px; overflow: hidden;
    box-shadow: 0 6px 18px rgba(0,0,0,0.18);
  }

  /* Brand name: plain, one colour, one weight */
  .brand {
    position: absolute; left: 0; right: 0;
    display: flex; align-items: center; justify-content: center; gap: 12px;
  }
  .brand-mark { display: block; flex: none; background: var(--blue); }
  .brand-name {
    font-family: "Michroma", sans-serif;
    font-weight: 400;
    white-space: nowrap;
  }

  /* Front */
  .card--front { background: var(--navy); }
  .card--front .brand { top: 118px; }
  .card--front .brand-mark { width: 20px; height: 20px; }
  .card--front .brand-name { font-size: 26px; color: var(--light-grey); }
  .front-rule {
    position: absolute; left: 0; right: 0; bottom: 40px;
    display: flex; align-items: center; gap: 12px;
  }
  .front-rule .line { height: 2px; background: var(--blue); }
  .front-rule .line--long { flex: 1; }
  .front-rule .line--short { width: 28px; }
  .rec-number {
    font-family: "Michroma", sans-serif;
    font-size: 11px; letter-spacing: 0.08em;
    color: var(--rec-text);
  }

  /* Back */
  .card--back { background: var(--white); }
  .card--back .brand { top: 56px; }
  .card--back .brand-mark { width: 16px; height: 16px; }
  .card--back .brand-name { font-size: 21px; color: var(--navy-text); }
  .holder {
    position: absolute; left: 0; right: 0; top: 150px;
    display: flex; align-items: center; justify-content: center; gap: 16px;
  }
  .holder .line { width: 96px; height: 2px; background: var(--blue); }
  .holder-name {
    font-family: "Michroma", sans-serif;
    font-size: 18px; letter-spacing: 0.1em;
    color: var(--navy-text); text-transform: uppercase;
  }
  .holder-role {
    position: absolute; left: 0; right: 0; top: 180px;
    text-align: center;
    font-family: "Open Sans", sans-serif; font-size: 12px;
    color: var(--grey-text);
  }
  .contact-list {
    position: absolute; left: 0; right: 0; top: 214px;
    list-style: none;
    display: flex; flex-direction: column; align-items: center; gap: 8px;
    font-family: "Open Sans", sans-serif; font-size: 14px;
    color: var(--grey-text);
  }
  .contact-list li { display: flex; align-items: center; gap: 10px; }
  .contact-list svg { width: 14px; height: 14px; fill: var(--blue); }
</style>
</head>
<body>
<main class="sheet">
  <section class="card card--front" aria-label="Card front">
    <div class="brand">
      <span class="brand-mark" aria-hidden="true"></span>
      <h1 class="brand-name">Volt'n Electrical</h1>
    </div>
    <div class="front-rule">
      <span class="line line--long"></span>
      <span class="rec-number">REC 48193</span>
      <span class="line line--short"></span>
    </div>
  </section>

  <section class="card card--back" aria-label="Card back">
    <div class="brand">
      <span class="brand-mark" aria-hidden="true"></span>
      <h2 class="brand-name">Volt'n Electrical</h2>
    </div>
    <div class="holder">
      <span class="line"></span>
      <span class="holder-name">Owen Tate</span>
      <span class="line"></span>
    </div>
    <p class="holder-role">Qualified Electrician</p>
    <ul class="contact-list">
      <li>
        <svg viewBox="0 0 24 24" aria-hidden="true"><path d="M6.6 10.8a15.1 15.1 0 0 0 6.6 6.6l2.2-2.2c.3-.3.7-.4 1-.2 1.1.4 2.3.6 3.6.6.6 0 1 .4 1 1V20c0 .6-.4 1-1 1A17 17 0 0 1 3 4c0-.6.4-1 1-1h3.5c.6 0 1 .4 1 1 0 1.3.2 2.5.6 3.6.1.3 0 .7-.2 1z"/></svg>
        0438257109
      </li>
      <li>
        <svg viewBox="0 0 24 24" aria-hidden="true"><path d="M2 5h20v14H2z"/><path d="M3.5 6.5 12 13l8.5-6.5" fill="none" stroke="#fff" stroke-width="1.5"/></svg>
        voltnelectrical@mailbox-example.net
      </li>
    </ul>
  </section>
</main>
</body>
</html>
```